Orla_Rendercraft Web Design Project

Orla Rendercraft wants a modern looking 1 page website that clearly emphasises the 3 specialised construction services:
1. Plastering = (inside walls etc)
2. Rendering = (outside walls etc)
3. Cornicing = (inside wall and ceilings)

Orla Rendercraft is run by craftsmen, so be creative.

I really like http://quorvitstudio.example

The site design lends itself well to being a one pager - I like the html click thru panel (at the base above the fold) that allows reader to stay on the one page but can see see more info by tapping on the red arrows.

The site is also successful because it doesn't rely on photos - but makes the most of big headlines and client testimonials.

I could provide you with more content if you need it to achieve this kind of site.
Updates

Project Deadline Extended
Reason: Hi, we have decided to extend the deadline as we have only received ideas from one designer. We feel there is still scope to improve on the designs we have received so far. Improvements in the following areas: - design that complements the new logo design (the logo shows that ORLA provide services inside and outside the house) - the design doesn't look like one of the many 'template' designs you see these days - the design does not need to use photos - if you can illustrate well as well as design website you will have an advantage! - site should look very modern / up to date We have now guaranteed payment in case designers were holding off.

Target Market(s)

Architects, interior designers, builders, home owners

Industry/Entity Type

Construction

Requirements
Must have
• Design at 1024 x 768
Website design should complement new logo - with black and ivory being dominant colours. (Logo is attached)
The site should be creative - as creativity is one of the key aspects of the service provide by Orla Rendercraft.
Text for the site has been provided - see pdf
Nice to have
• It's not essential to use photos. In the quick example I have attached I have sourced photos from pixbarnshots.example
File #: 8394027 / File #: 40958312 / File #: 9127485. I repeat photos are not mandatory - you may prefer to use other graphical devices.
Easily coded
Modern looking design

```html
<!DOCTYPE html>
<html lang="en">
<head>
<meta charset="utf-8">
<title>Orla Rendercraft – Plastering, Rendering &amp; Cornicing</title>
<link rel="stylesheet" href="https://fonts.googleapis.com/css2?family=Rye&family=Oswald:wght@400&family=Roboto+Condensed:wght@400&family=Roboto+Slab:wght@500&family=Libre+Baskerville&family=Arimo&display=swap">
<style>
:root{
  --black:#000;
  --ivory:#f3e8cc;
  --ivory-dark:#e9dab4;
  --gold:#b08a3c;
  --orange:#f5a821;
  --grey-head:#8a8a8a;
  --grey-text:#7c7c7c;
  --card-border:#d8d8d8;
  --footer-text:#f4e28a;
  --white:#fff;
}
*{box-sizing:border-box;margin:0;padding:0}
html,body{width:1200px;height:918px;overflow:hidden;background:var(--white)}
.page{position:relative;width:1200px;height:918px;font-family:"Arimo",Arial,sans-serif}

.site-header{position:absolute;left:0;top:0;width:1200px;height:65px;background:var(--black)}
.brand{position:absolute;left:36px;top:14px;display:flex;align-items:center;gap:8px;color:var(--white);font-family:"Roboto Condensed",sans-serif;font-size:24px;letter-spacing:2px}
.brand-mark{width:14px;height:14px;background:var(--white)}
.main-nav{position:absolute;right:36px;top:0;height:65px;display:flex;align-items:center}
.main-nav a{color:var(--white);text-decoration:none;font-family:"Roboto Condensed",sans-serif;font-size:20px;padding:0 20px;border-left:1px solid #444;line-height:38px}
.main-nav a:first-child{border-left:none}

.hero{position:absolute;left:0;top:65px;width:1200px;height:289px;background:radial-gradient(ellipse at 40% 40%,var(--ivory) 0%,var(--ivory-dark) 100%);border-bottom:3px solid var(--gold)}
.hero-title{position:absolute;left:26px;top:45px;font-family:"Rye",serif;font-weight:400;font-size:50px;line-height:68px;color:var(--white);-webkit-text-stroke:1.5px #2a1a0a;text-shadow:3px 3px 0 #2a1a0a;letter-spacing:1px}
.hero-cta{position:absolute;left:26px;top:213px;width:289px;height:47px;border-radius:8px;border:1px solid #e2c76a;background:linear-gradient(#fffbe6,#ffe49a 55%,#f8cf60);font-family:"Oswald",sans-serif;font-size:24px;color:#1a1a1a;display:flex;align-items:center;justify-content:center;text-decoration:none;box-shadow:0 1px 2px rgba(0,0,0,.15)}

.service{position:absolute;top:372px;width:361px;height:168px;border:2px solid var(--card-border);border-radius:6px;background:var(--white);box-shadow:0 8px 8px -6px rgba(0,0,0,.18)}
.service.plastering{left:26px}
.service.rendering{left:414px}
.service.cornicing{left:801px}
.service h2{position:absolute;left:14px;top:4px;font-family:"Roboto Slab",serif;font-weight:500;font-size:28px;color:#151515}
.service .rule{position:absolute;left:14px;right:14px;top:44px;border-top:1px dashed #999}
.service ul{position:absolute;left:22px;top:52px;width:240px;list-style:none;font-family:"Libre Baskerville",serif;font-size:15px;line-height:20px;color:#222}
.service li{position:relative;padding-left:16px;margin-bottom:7px}
.service li::before{content:"";position:absolute;left:2px;top:6px;border-left:5px solid var(--orange);border-top:4px solid transparent;border-bottom:4px solid transparent}
.service .tool{position:absolute;right:22px;bottom:18px;width:76px;height:48px;border-radius:4px;background:linear-gradient(135deg,#e8e8e8,#b9b9b9)}
.service.rendering .tool{background:linear-gradient(135deg,#c9b39a,#8a7765)}
.service.cornicing .tool{width:48px;height:80px;right:22px;background:linear-gradient(#faf2dd,#e9d9b4)}

.info{position:absolute;top:570px;width:537px}
.info.about{left:25px}
.info.works{left:627px}
.info h2{font-family:"Roboto Condensed",sans-serif;font-weight:400;font-size:30px;color:var(--grey-head);padding-bottom:6px;border-bottom:1px dashed #aaa}
.info h2 span{color:var(--orange)}
.info p{margin-top:14px;font-size:13.5px;line-height:20px;color:var(--grey-text)}

.gallery{position:absolute;left:633px;top:720px;width:527px;height:77px}
.gallery .arrow{position:absolute;top:27px}
.gallery .prev{left:0}
.gallery .next{right:0}
.thumb{position:absolute;top:0;width:103px;height:77px;border:1px solid #c9a55a}
.thumb.t1{left:37px;background:linear-gradient(135deg,#fff3a0,#f3d54a)}
.thumb.t2{left:154px;background:linear-gradient(135deg,#c46a3a,#8e3f1e)}
.thumb.t3{left:271px;background:linear-gradient(135deg,#f4e3c6,#b99464)}
.thumb.t4{left:388px;background:linear-gradient(135deg,#e7b36a,#8b5a2a)}

.site-footer{position:absolute;left:0;top:816px;width:1200px;height:102px;background:var(--black);border-top:3px solid var(--gold);font-family:"Libre Baskerville",serif;color:var(--footer-text);font-size:15px}
.footer-contact{position:absolute;left:25px;top:27px;line-height:21px}
.footer-copy{position:absolute;right:40px;top:54px}
</style>
</head>
<body>
<div class="page">
  <header class="site-header">
    <div class="brand"><span class="brand-mark"></span>ORLA RENDERCRAFT</div>
    <nav class="main-nav">
      <a href="#about">About Us</a>
      <a href="#works">Our Work</a>
      <a href="#testimonial">Testimonial</a>
      <a href="#contact">Contact Us</a>
    </nav>
  </header>

  <section class="hero">
    <h1 class="hero-title">We are a complete solution for your<br>home plastering ...</h1>
    <a class="hero-cta" href="#contact">CONTACT US</a>
  </section>

  <article class="service plastering">
    <h2>Plastering</h2><div class="rule"></div>
    <ul>
      <li>Solid plastering, including hard plaster, stucco, white set.</li>
      <li>Mouldings</li>
      <li>Plasterboard</li>
    </ul>
    <div class="tool" role="img" aria-label="Plastering trowel"></div>
  </article>
  <article class="service rendering">
    <h2>Rendering</h2><div class="rule"></div>
    <ul>
      <li>Cement render</li>
      <li>Acrylic render</li>
      <li>Specialised coatings</li>
    </ul>
    <div class="tool" role="img" aria-label="Rendering trowel"></div>
  </article>
  <article class="service cornicing">
    <h2>Cornicing</h2><div class="rule"></div>
    <ul>
      <li>Custom &amp; off the shelf cornices</li>
      <li>Ornamental roses</li>
    </ul>
    <div class="tool" role="img" aria-label="Cornice profile"></div>
  </article>

  <section class="info about" id="about">
    <h2>About <span>Orla Rendercraft, Melbourne</span></h2>
    <p>We are specialists in all aspects of plastering, rendering and cornicing throughout Melbourne. We undertake residential and commercial projects of all sizes, including home renovations, new builds and specialised architectural projects.</p>
  </section>
  <section class="info works" id="works">
    <h2>Our <span>Works</span></h2>
    <p>We are specialists in all aspects of plastering, rendering and cornicing throughout Melbourne. We undertake residential and commercial projects of all sizes, including home renovations, new builds and specialised architectural projects.</p>
  </section>

  <div class="gallery">
    <svg class="arrow prev" width="22" height="24" viewBox="0 0 22 24"><polygon points="22,0 0,12 22,24" fill="#000"/></svg>
    <div class="thumb t1" role="img" aria-label="Yellow feature wall project"></div>
    <div class="thumb t2" role="img" aria-label="Textured render project"></div>
    <div class="thumb t3" role="img" aria-label="Bathroom plastering project"></div>
    <div class="thumb t4" role="img" aria-label="Hallway plastering project"></div>
    <svg class="arrow next" width="22" height="24" viewBox="0 0 22 24"><polygon points="0,0 22,12 0,24" fill="#000"/></svg>
  </div>

  <footer class="site-footer" id="contact">
    <div class="footer-contact">Orla Rendercraft | Tel: 0412 836 905<br>&nbsp;Email: info@orlarendercraft.example</div>
    <div class="footer-copy">© 2011, All Rights Reserved</div>
  </footer>
</div>
</body>
</html>
```